Healthcare technology firm needs business card layout. Logo provided.

We need a business card design for a new healthcare technology company called Kevrimo.com. The logo is already done so that will be used in the design. We assist patients and their families manage their personal health finances. Our initial product is our web site membership that includes educational content on your health benefits, tools, and downloadable forms.

We would like to see designs that use our existing logo or extend the logo in a creative way. Should be very consumer friendly.

```html
<!DOCTYPE html>
<html lang="en">
<head>
<meta charset="utf-8">
<title>Kevrimo.com — Business Card</title>
<link href="https://fonts.googleapis.com/css2?family=Arimo:wght@400;700&family=Montserrat:wght@500;600&display=swap" rel="stylesheet">
<style>
  :root {
    --bg-light: #f2f2f6;
    --bg-mid: #c9c9d3;
    --card-core: #2b2a7c;
    --card-edge: #0c0b36;
    --brand-green: #7fca3f;
    --text-green: #8fd24c;
    --name-grey: #c9c9d2;
    --band-dark: #0c4f8e;
    --band-light: #1f8fd0;
    --band-text: #e8f2fb;
    --rule: #5d5f6e;
    --web-teal: #1b8f8a;
  }
  * { box-sizing: border-box; margin: 0; padding: 0; }
  html, body { width: 1200px; height: 900px; overflow: hidden; }
  body {
    background: linear-gradient(100deg, var(--bg-mid) 0%, var(--bg-light) 30%, var(--bg-light) 70%, var(--bg-mid) 100%);
    font-family: "Arimo", Arial, sans-serif;
    position: relative;
  }
  .card {
    position: absolute;
    left: 290px;
    width: 620px;
    height: 354px;
    border-radius: 24px;
    background: radial-gradient(ellipse at 50% 45%, var(--card-core) 0%, #1b1a5e 45%, var(--card-edge) 100%);
    box-shadow: 0 10px 24px rgba(20, 20, 50, 0.35);
    overflow: hidden;
  }
  .card--front { top: 70px; }
  .card--back { top: 470px; }

  .wordmark {
    position: absolute;
    left: 0; right: 0;
    text-align: center;
    font-family: "Arimo", Arial, sans-serif;
    font-weight: 700;
    color: var(--brand-green);
    letter-spacing: 2px;
  }
  .card--front .wordmark { top: 34px; font-size: 62px; }
  .card--back .wordmark { top: 118px; font-size: 66px; }

  .holder { position: absolute; left: 58px; top: 168px; }
  .holder__name { font-size: 25px; font-weight: 700; color: var(--name-grey); letter-spacing: 0.5px; }
  .holder__role { font-size: 19px; color: var(--text-green); margin-top: 6px; }

  .divider {
    position: absolute; left: 300px; top: 146px;
    width: 2px; height: 96px; background: var(--rule);
  }

  .contact { position: absolute; left: 326px; top: 138px; list-style: none; }
  .contact__item {
    display: flex; align-items: flex-start; gap: 10px;
    font-size: 16px; color: var(--text-green); line-height: 20px; margin-bottom: 6px;
  }
  .contact__icon { width: 16px; height: 16px; flex: none; margin-top: 2px; }
  .contact__lines span { display: block; }
  .contact__lines span + span { padding-left: 10px; }

  .band-rule {
    position: absolute; left: 0; right: 0; height: 4px;
    background: var(--band-dark);
  }
  .band-rule--top { top: 262px; }
  .band-rule--bottom { top: 322px; height: 8px; background: linear-gradient(90deg, var(--band-dark), var(--band-light)); }
  .tagline-band {
    position: absolute; left: 0; right: 0; top: 272px; height: 42px;
    background: linear-gradient(90deg, var(--band-dark) 0%, var(--band-light) 60%, #2aa0de 100%);
    display: flex; align-items: center; justify-content: center;
    font-family: "Montserrat", Arial, sans-serif; font-weight: 500;
    font-size: 18px; color: var(--band-text); letter-spacing: 0.5px;
  }

  .web-address {
    position: absolute; left: 0; right: 0; top: 204px;
    text-align: center;
    font-family: "Montserrat", Arial, sans-serif; font-weight: 600;
    font-size: 24px; color: var(--web-teal); letter-spacing: 1.5px;
  }
</style>
</head>
<body>
  <section class="card card--front" aria-label="Business card front">
    <div class="wordmark">KEVRIMO</div>

    <div class="holder">
      <p class="holder__name">DANA M. ORTIS</p>
      <p class="holder__role">CEO</p>
    </div>

    <div class="divider"></div>

    <ul class="contact">
      <li class="contact__item">
        <svg class="contact__icon" viewBox="0 0 16 16" aria-hidden="true"><path d="M2 8 L8 2.5 L14 8 M4 7 V14 H12 V7" fill="none" stroke="#c9c9d2" stroke-width="1.6"/><rect x="7" y="10" width="2.4" height="4" fill="#c9c9d2"/></svg>
        <div class="contact__lines"><span>Riverton Cedar Falls</span><span>Mapleton Eastport</span></div>
      </li>
      <li class="contact__item">
        <svg class="contact__icon" viewBox="0 0 16 16" aria-hidden="true"><rect x="4.5" y="1.5" width="7" height="13" rx="1.5" fill="none" stroke="#c9c9d2" stroke-width="1.5"/><rect x="6" y="3.5" width="4" height="4" fill="#c9c9d2"/></svg>
        <div class="contact__lines"><span>555-014-2297</span></div>
      </li>
      <li class="contact__item">
        <svg class="contact__icon" viewBox="0 0 16 16" aria-hidden="true"><circle cx="8" cy="8" r="6.2" fill="none" stroke="#c9c9d2" stroke-width="1.4"/><path d="M1.8 8 H14.2 M8 1.8 C4.8 5 4.8 11 8 14.2 M8 1.8 C11.2 5 11.2 11 8 14.2" fill="none" stroke="#c9c9d2" stroke-width="1.2"/></svg>
        <div class="contact__lines"><span>www.kevrimo.com</span></div>
      </li>
    </ul>

    <div class="band-rule band-rule--top"></div>
    <div class="tagline-band">Making Your Health Costs Simpler</div>
    <div class="band-rule band-rule--bottom"></div>
  </section>

  <section class="card card--back" aria-label="Business card back">
    <div class="wordmark">KEVRIMO</div>
    <div class="web-address">www.kevrimo.com</div>
  </section>
</body>
</html>
```